Business Card Design for Orthopaedic Surgeon

This is a double-sided glossy business card. I prefer baby blue, teal, and green as color schemes. I have my logo already (many colors that you can choose from). I have photos and examples of my old card (very bland but has the information in it). I also have one that my assistant tried to design, but the writing is too small and I don't love the formatting. But it is close!
I would like my logo to be on the business card but I'm uploading my logo in many different colors so you can choose which one looks best based on the color scheme. I also uploaded many sized headshots so you can choose the best resolution one.

Additional information:
Correct business address:
4382 SE 58th Lane, Suite 305
Tamarac, FL 33347

Everything else on both business cards are accurate.

I actually need 2 different business cards generated. One that includes my cell phone number-- Personal cell: 585-614-3908 in addition to Office phone: (954) 362-5804 and Office Fax: 954-362-5819. Again, one card would have my personal cell and one wouldn't

Overall I just think the baby blue card (uploaded) is missing something on the front--of course it is also missing my office phone/fax/personal cell. I do want my website on the front too. Email: info@rkellowsurg.com

You can use your discretion about what goes on the front vs. what goes on the back to eliminated clutter.

Oh and on the back, I would like to list "Conditions Treated" (not specialties include). The list is:
Carpal Tunnel
Trigger Finger
Ganglion Cysts
Hand Tumors
Han & Wrist Arthritis
Hand, Wrist & Elbow Tendonitis
Fractures of the Hand, Wrist, Elbow and Humerus
Nerve Injuries of the Hand, Wrist & Elbow
Microsurgery
Wrist Arthroscopy
Endoscopic Surgery

Target Market(s)

Primary care doctors, Lawyers, patients

Industry/Entity Type

Medical

Contact Information for Business Card

Please see above in project description

Colors

Requirements
Must have
• -Correct office info, Board Certified Orthopaedic Hand & Upper Extremity Surgeon
Nice to have
• Something that is classy and wow!

```html
<!DOCTYPE html>
<html lang="en">
<head>
<meta charset="utf-8">
<title>Renata Kellow M.D. — Business Card</title>
<link href="https://fonts.googleapis.com/css2?family=Comfortaa:wght@300;500;600;700&family=Montserrat:wght@700&display=swap" rel="stylesheet">
<style>
  :root {
    --stage: #2f3439;
    --navy: #06233a;
    --navy-deep: #031726;
    --glow: #2394d6;
    --sky: #2a9ad8;
    --ink: #111111;
    --grey: #5a5a5a;
    --white: #ffffff;
    --photo-a: #d9d9d9;
    --photo-b: #3a3a3a;
  }
  * { margin: 0; padding: 0; box-sizing: border-box; }
  html, body { width: 1200px; height: 1147px; overflow: hidden; }
  body {
    background: var(--stage);
    position: relative;
    font-family: "Comfortaa", sans-serif;
  }
  .card {
    position: absolute;
    top: 427px;
    width: 512px;
    height: 293px;
    overflow: hidden;
  }

  /* Front */
  .card-front { left: 70px; background: var(--white); }
  .card-front .edge-strip {
    position: absolute; right: 0; top: 0; width: 29px; height: 100%;
    background: var(--navy);
  }
  .doctor-name {
    position: absolute; left: 20px; top: 40px;
    font-family: "Montserrat", sans-serif; font-weight: 700;
    font-size: 25.5px; line-height: 30px; letter-spacing: -0.5px; color: var(--ink);
    white-space: nowrap;
  }
  .doctor-name .first { color: var(--sky); }
  .doctor-title {
    position: absolute; left: 20px; top: 72px; width: 290px;
    text-align: center; font-weight: 300; font-size: 15px;
    line-height: 21px; color: var(--grey); white-space: nowrap;
  }
  .contact-panel {
    position: absolute; left: 0; top: 125px; width: 254px; height: 100px;
    background: var(--navy); padding: 7px 0 0 26px;
    list-style: none;
  }
  .contact-panel li {
    display: flex; align-items: center; gap: 13px;
    height: 23.5px; color: var(--white);
    font-weight: 700; font-size: 15.5px; white-space: nowrap;
  }
  .contact-panel svg { width: 13px; height: 13px; fill: var(--white); flex: none; }
  .address {
    position: absolute; left: 36px; top: 234px;
    font-size: 16px; line-height: 21px; color: var(--ink); font-weight: 300;
    white-space: nowrap;
  }
  .headshot {
    position: absolute; left: 315px; top: 50px; width: 168px; height: 243px;
    background: radial-gradient(ellipse at 50% 35%, var(--photo-a) 0%, #8a8a8a 45%, var(--photo-b) 100%);
    border-radius: 80px 80px 0 0;
  }

  /* Back */
  .card-back {
    left: 614px;
    background: radial-gradient(ellipse 55% 75% at 42% 62%, var(--glow) 0%, #0f5f94 35%, var(--navy) 70%, var(--navy-deep) 100%);
    color: var(--white);
  }
  .conditions-title {
    position: absolute; left: 34px; top: 22px;
    font-weight: 700; font-size: 16px; line-height: 20px; white-space: nowrap;
  }
  .conditions-list {
    position: absolute; left: 57px; top: 50px; list-style: none;
  }
  .conditions-list li {
    position: relative; padding-left: 21px;
    font-weight: 600; font-size: 14.5px; line-height: 20.4px; white-space: nowrap;
  }
  .conditions-list li::before {
    content: ""; position: absolute; left: 0; top: 8px;
    width: 5px; height: 5px; border-radius: 50%; background: var(--white);
  }
  .practice-mark {
    position: absolute; left: 345px; top: 82px;
    display: flex; align-items: center; gap: 8px; white-space: nowrap;
  }
  .practice-mark .dot {
    width: 16px; height: 16px; border-radius: 50%; border: 2px solid var(--white); flex: none;
  }
  .practice-mark .name {
    font-weight: 700; font-size: 14px; color: var(--white); letter-spacing: 1px;
  }
</style>
</head>
<body>
  <section class="card card-front" aria-label="Business card front">
    <div class="edge-strip"></div>
    <h1 class="doctor-name"><span class="first">RENATA</span> KELLOW M.D.</h1>
    <p class="doctor-title">Board Certified Orthopedic<br>Hand &amp; Upper Extremity Surgeon</p>
    <ul class="contact-panel">
      <li>
        <svg viewBox="0 0 24 24"><path d="M6.6 10.8a15.1 15.1 0 0 0 6.6 6.6l2.2-2.2a1 1 0 0 1 1-.25 11.4 11.4 0 0 0 3.6.57 1 1 0 0 1 1 1V20a1 1 0 0 1-1 1A17 17 0 0 1 3 4a1 1 0 0 1 1-1h3.5a1 1 0 0 1 1 1c0 1.25.2 2.45.57 3.6a1 1 0 0 1-.25 1z"/></svg>
        (954) 362-5804
      </li>
      <li>
        <svg viewBox="0 0 24 24"><path d="M6 2h12v5H6zM3 8h18a1 1 0 0 1 1 1v8h-4v5H6v-5H2V9a1 1 0 0 1 1-1zm5 8v4h8v-4z"/></svg>
        (954) 362-5819
      </li>
      <li>
        <svg viewBox="0 0 24 24"><path d="M2 5h20v2l-10 6L2 7zm0 4 10 6 10-6v10H2z"/></svg>
        info@rkellowsurg.com
      </li>
      <li>
        <svg viewBox="0 0 24 24"><path d="M12 2a10 10 0 1 0 0 20 10 10 0 0 0 0-20zm7.9 9h-3.4a15 15 0 0 0-1.3-5.6A8 8 0 0 1 19.9 11zM12 4c.9 1.3 2.1 3.8 2.4 7H9.6c.3-3.2 1.5-5.7 2.4-7zM8.8 5.4A15 15 0 0 0 7.5 11H4.1a8 8 0 0 1 4.7-5.6zM4.1 13h3.4a15 15 0 0 0 1.3 5.6A8 8 0 0 1 4.1 13zm7.9 7c-.9-1.3-2.1-3.8-2.4-7h4.8c-.3 3.2-1.5 5.7-2.4 7zm3.2-1.4a15 15 0 0 0 1.3-5.6h3.4a8 8 0 0 1-4.7 5.6z"/></svg>
        www.rkellowsurg.com
      </li>
    </ul>
    <p class="address">4382 SE 58th Lane, Suite 305<br>Tamarac, FL 33347</p>
    <div class="headshot" role="img" aria-label="Headshot portrait of the surgeon in a dark blazer"></div>
  </section>

  <section class="card card-back" aria-label="Business card back">
    <h2 class="conditions-title">CONDITIONS TREATED</h2>
    <ul class="conditions-list">
      <li>Carpal Tunnel</li>
      <li>Trigger Finger</li>
      <li>Ganglion Cysts</li>
      <li>Hand Tumors</li>
      <li>Hand &amp; Wrist Arthritis</li>
      <li>Hand, Wrist &amp; Elbow Tendonitis</li>
      <li>Fractures of the Hand, Wrist, Elbow &amp; Humerus</li>
      <li>Nerve Injuries of the Hand, Wrist &amp; Elbow</li>
      <li>Microsurgery</li>
      <li>Wrist Arthroscopy</li>
      <li>Endoscopic Surgery</li>
    </ul>
    <div class="practice-mark">
      <span class="dot"></span>
      <span class="name">KELLOW HAND</span>
    </div>
  </section>
</body>
</html>
```